Google Form Graphic to suit our Brand and industry

Create a graphic / image for us to put at the top of our client enquiry google form.
The image will be a section of an architectural home with our branding over the top. Preferably translucent.
The image must suit the shape of the google forms image, which is an elongated rectangle
#003d5d - brand colour

Target Market(s)

residential home owners, high end architectural homes

Industry/Entity Type

Residential construction

Colors
0054AA
0677BA
7BADD7
CADEEF
E8F1F8

Requirements
Must have
• our branding and a photo of an architectural home in the background

```html
<!DOCTYPE html>
<html lang="en">
<head>
<meta charset="utf-8">
<title>New Client Enquiry Form – Header</title>
<link href="https://fonts.googleapis.com/css2?family=Roboto:wght@400;500&display=swap" rel="stylesheet">
<style>
  :root {
    --page-cream: #f7efdf;
    --brand-navy: #003d5d;
    --accent-gold: #e0b762;
    --rule-bronze: #7a5c1e;
    --card-white: #ffffff;
    --card-edge: #e6e1d6;
    --focus-blue: #4285f4;
    --text-dark: #202124;
    --text-muted: #70757a;
    --icon-grey: #5f6368;
    --required-red: #d93025;
    --forest-deep: #2f4a33;
    --forest-mid: #5d7f55;
    --sky-pale: #c9d7cf;
    --terrace-light: #d9dcd6;
    --wordmark-white: #ffffff;
  }
  * { box-sizing: border-box; margin: 0; padding: 0; }
  html, body {
    width: 1200px; height: 952px; overflow: hidden;
    background: var(--page-cream);
    font-family: "Roboto", Arial, sans-serif;
  }
  .canvas { position: relative; width: 1200px; height: 952px; }

  .header-banner {
    position: absolute; left: 53px; top: 18px; width: 1124px; height: 282px;
    border-radius: 10px; overflow: hidden;
  }
  .header-banner svg { position: absolute; inset: 0; }
  .brand-name {
    position: absolute; left: 66px; top: 112px;
    font-family: "Roboto", Arial, sans-serif; font-weight: 500;
    font-size: 50px; line-height: 58px; letter-spacing: 0;
    color: var(--wordmark-white); white-space: nowrap;
  }

  .theme-tab {
    position: absolute; left: 52px; top: 318px; width: 175px; height: 30px;
    background: var(--accent-gold); border-radius: 7px 7px 0 0;
  }
  .theme-band {
    position: absolute; left: 52px; top: 344px; width: 1120px; height: 41px;
    background: var(--accent-gold);
  }

  .form-card {
    position: absolute; left: 52px; width: 1120px;
    background: var(--card-white); border: 1px solid var(--card-edge);
    border-radius: 9px;
  }
  .title-card { top: 385px; height: 243px; border-top: none; border-radius: 0 0 9px 9px; }
  .form-title {
    position: absolute; left: 36px; top: 38px;
    font-size: 45px; font-weight: 400; color: var(--text-dark);
  }
  .title-rule {
    position: absolute; left: 35px; top: 100px; width: 926px; height: 2px;
    background: var(--rule-bronze);
  }
  .format-tools { position: absolute; left: 55px; top: 120px; display: flex; gap: 34px; }
  .format-tools svg { width: 24px; height: 24px; }
  .card-actions { position: absolute; right: 40px; top: 42px; display: flex; gap: 45px; }
  .form-description {
    position: absolute; left: 36px; top: 178px;
    font-size: 19px; color: var(--text-dark);
  }

  .question-card { top: 648px; height: 201px; border-left: 8px solid var(--focus-blue); }
  .question-text {
    position: absolute; left: 40px; top: 38px; font-size: 23px; color: var(--text-dark);
  }
  .required-mark { color: var(--required-red); margin-left: 14px; }
  .answer-placeholder {
    position: absolute; left: 28px; top: 108px; font-size: 18px; color: var(--text-muted);
  }
  .answer-line {
    position: absolute; left: 28px; top: 139px; width: 525px;
    border-bottom: 2px dotted #9aa0a6;
  }

  .field-card { top: 868px; height: 110px; }
  .field-label { position: absolute; left: 36px; top: 40px; font-size: 22px; color: var(--text-dark); }
</style>
</head>
<body>
<main class="canvas">

  <header class="header-banner">
    <svg width="1124" height="282" viewBox="0 0 1124 282">
      <defs>
        <linearGradient id="homePhotoTone" x1="0" y1="0" x2="1" y2="1">
          <stop offset="0" stop-color="#c9d7cf"/>
          <stop offset="0.35" stop-color="#5d7f55"/>
          <stop offset="0.7" stop-color="#2f4a33"/>
          <stop offset="1" stop-color="#d9dcd6"/>
        </linearGradient>
      </defs>
      <rect class="home-photo" width="1124" height="282" fill="url(#homePhotoTone)"
            role="img" aria-label="Photo of a modern glass-walled architectural home in a forest beside a pool"/>
      <path class="brand-panel" d="M0 0 H420 L330 95 Q305 143 330 190 L423 282 H0 Z" fill="#003d5d"/>
    </svg>
    <div class="brand-name">Meridian Build</div>
  </header>

  <div class="theme-tab"></div>
  <div class="theme-band"></div>

  <section class="form-card title-card">
    <h1 class="form-title">New Client Enquiry Form</h1>
    <div class="title-rule"></div>
    <div class="format-tools" aria-hidden="true">
      <svg viewBox="0 0 24 24"><text x="4" y="20" font-family="Roboto, sans-serif" font-weight="500" font-size="22" fill="#5f6368">B</text></svg>
      <svg viewBox="0 0 24 24"><text x="5" y="20" font-family="Roboto, sans-serif" font-style="italic" font-weight="500" font-size="22" fill="#5f6368">I</text></svg>
      <svg viewBox="0 0 24 24"><text x="5" y="18" font-family="Roboto, sans-serif" font-size="21" fill="#5f6368">U</text><rect x="4" y="21" width="16" height="2" fill="#5f6368"/></svg>
      <svg viewBox="0 0 24 24"><rect x="2" y="8" width="20" height="8" rx="4" fill="none" stroke="#5f6368" stroke-width="2.2"/><line x1="8" y1="12" x2="16" y2="12" stroke="#5f6368" stroke-width="2.2"/></svg>
      <svg viewBox="0 0 24 24"><path d="M5 4 H20 M12 4 L9 20 M4 6 L20 22" stroke="#5f6368" stroke-width="2.2" fill="none"/></svg>
    </div>
    <div class="card-actions" aria-hidden="true">
      <svg width="16" height="24" viewBox="0 0 16 24"><path d="M3 2 L8 7 L13 2 M3 22 L8 17 L13 22" stroke="#5f6368" stroke-width="2" fill="none"/></svg>
      <svg width="6" height="24" viewBox="0 0 6 24"><circle cx="3" cy="3" r="2.6" fill="#5f6368"/><circle cx="3" cy="12" r="2.6" fill="#5f6368"/><circle cx="3" cy="21" r="2.6" fill="#5f6368"/></svg>
    </div>
    <p class="form-description">We would love to hear your thoughts or feedback on how we can improve your experience!</p>
  </section>

  <section class="form-card question-card">
    <p class="question-text">Firstly, how did you hear about us?<span class="required-mark">*</span></p>
    <p class="answer-placeholder">Short answer text</p>
    <div class="answer-line"></div>
  </section>

  <section class="form-card field-card">
    <p class="field-label">Name</p>
  </section>

</main>
</body>
</html>
```